Tandem Roster survey and prize

We need an A4 poster design for a survey and competition I wish to hold. The survey will be on Poll Heron. My website www.example.com.au will redirect the users to the survey page. I will be selecting a survey entrant at random to win a prize. The prize is $200 cash. The survey will be open for two months as the mail out of this poster will go throughout Victoria, Australia. The competition end date is yet to be decided - depends on when I can get this poster completed and the mail out done.

The mail out is targeting the Aged Care industry workers and decision makers. It hopefully will be placed on a notice board in the facilities and need to attract attention for people to visit my site and then take the survey.

The survey is for not for residents but for the workers in the facility.

Reason: Just got some feedback on required content of the poster. Text for the poster required: "The survey is for determining a market for rostering and payroll software, your assitance in taking this survey would be greatly appreciated." Martin Hale

Target Market(s)

Workers in Aged Care industry and decision makers.

Industry/Entity Type

Industry

Requirements
Must have
• 1. Must reference the website www.example.com.au.
2. Must mention that there is a prize of $200.
3. Must mention that entry to the competition is dependant on taking the survey.
4. Must mention the close date (date yet to be decided).
5. Must mention winning contestant will be contacted by phone.

```html
<!DOCTYPE html>
<html lang="en">
<head>
<meta charset="utf-8">
<title>How's Work Going? – Survey Poster</title>
<link rel="stylesheet" href="https://fonts.googleapis.com/css2?family=Open+Sans:ital,wght@0,400;0,800;1,400&family=Archivo+Black&display=swap">
<style>
  :root {
    --sky: #0aaeea;
    --band: #1c9fdc;
    --scene-light: #2a9fd6;
    --scene-dark: #0f7fb6;
    --white: #ffffff;
    --prize-yellow: #fff200;
    --prize-shadow: #0d5a86;
    --note-bg: #e7e8e9;
    --note-text: #555555;
    --mascot: #2f7fc8;
  }
  html, body {
    margin: 0;
    padding: 0;
    overflow: hidden;
    background: var(--sky);
  }
  .poster {
    position: relative;
    width: 907px;
    height: 1200px;
    background: var(--sky);
    overflow: hidden;
    font-family: "Open Sans", Arial, sans-serif;
  }
  .headline {
    position: absolute;
    left: 0;
    top: 0;
    width: 907px;
    height: 360px;
  }
  .headline text {
    font-family: "Open Sans", Arial, sans-serif;
    font-weight: 800;
    fill: var(--white);
  }
  .mascot {
    position: absolute;
    border-radius: 50% 50% 45% 45%;
    background: var(--mascot);
  }
  .mascot--top { left: 606px; top: 26px; width: 64px; height: 56px; }
  .mascot--note { left: 734px; top: 1126px; width: 58px; height: 48px; }
  .scene {
    position: absolute;
    left: 58px;
    top: 408px;
    width: 818px;
    height: 430px;
    background: linear-gradient(180deg, var(--scene-light) 0%, var(--scene-dark) 100%);
    border-radius: 120px 120px 0 0;
  }
  .prize-band {
    position: absolute;
    left: 0;
    top: 838px;
    width: 907px;
    height: 362px;
    background: var(--band);
  }
  .prize-band svg { position: absolute; left: 0; top: 0; }
  .call { font-family: "Archivo Black", "Arial Black", sans-serif; fill: var(--white); }
  .prize { font-family: "Archivo Black", "Arial Black", sans-serif; }
  .prize-shadow { fill: var(--prize-shadow); }
  .prize-win { fill: var(--prize-yellow); }
  .prize-amount { fill: var(--white); }
  .details {
    position: absolute;
    left: 0;
    top: 1036px;
    width: 907px;
    margin: 0;
    text-align: center;
    color: var(--white);
    font-size: 18.5px;
    line-height: 27px;
  }
  .note {
    position: absolute;
    left: 127px;
    top: 1108px;
    width: 597px;
    height: 58px;
    box-sizing: border-box;
    padding: 10px 8px 0;
    background: var(--note-bg);
    border-radius: 6px;
    color: var(--note-text);
    font-size: 14px;
    letter-spacing: 0.55px;
    line-height: 20px;
    text-align: center;
    white-space: nowrap;
    margin: 0;
  }
  .note::after {
    content: "";
    position: absolute;
    right: -12px;
    top: 24px;
    border-left: 14px solid var(--note-bg);
    border-top: 7px solid transparent;
    border-bottom: 7px solid transparent;
  }
</style>
</head>
<body>
<main class="poster">
  <svg class="headline" viewBox="0 0 907 360" aria-label="How's work going?">
    <text x="88" y="165" font-size="126" textLength="748" lengthAdjust="spacingAndGlyphs">HOW’S WORK</text>
    <text x="74" y="338" font-size="228" textLength="762" lengthAdjust="spacingAndGlyphs">GOING?</text>
  </svg>
  <div class="mascot mascot--top" role="img" aria-label="Small blue bird mascot perched on the headline"></div>

  <div class="scene" role="img" aria-label="Illustration of an aged care worker in green scrubs and an elderly resident with a walking frame in a park with blue trees"></div>

  <section class="prize-band">
    <svg width="907" height="220" viewBox="0 0 907 220">
      <text class="call" x="65" y="44" font-size="38" textLength="780" lengthAdjust="spacingAndGlyphs">PARTICIPATE IN THE SURVEY AND BE IN TO</text>
      <g class="prize" font-size="150">
        <text class="prize-shadow" x="80" y="171" textLength="318" lengthAdjust="spacingAndGlyphs">WIN</text>
        <text class="prize-win" x="92" y="177" textLength="318" lengthAdjust="spacingAndGlyphs">WIN</text>
        <text class="prize-shadow" x="428" y="171" textLength="402" lengthAdjust="spacingAndGlyphs">$200</text>
        <text class="prize-amount" x="440" y="177" textLength="402" lengthAdjust="spacingAndGlyphs">$200</text>
      </g>
    </svg>
  </section>

  <p class="details">Please take the time to fill in this survey at www.example.com.au to enter the draw.<br>Hurry! survey closes on&nbsp; 00/00/2012 and the winner will be contacted by phone.</p>

  <p class="note">“The survey is for determining a market for rostering and payroll software,<br>your assistance in taking this survey would be greatly appreciated.”</p>
  <div class="mascot mascot--note" role="img" aria-label="Small blue bird mascot speaking the note"></div>
</main>
</body>
</html>
```